LoomTrellis business card & letterhead
LoomTrellis letterhead and envelopes
I want to thank everyone for your great artwork. I really appreciate all of the inputs. Thank you again.
Pls check private message
Thanks
Paloma pixel
Nice drafts. Thank you all. Keep them coming. Please do not place a bar in the middle of the card.
Again: the title after the name is Ed.S.
So: Howard Winslow Ed.S.
I like the swirl (cycle) better than the straight lines.
Just keep it to single sided please.
Ok, I forgot to put my degree on the guide. It should be: Howard Winslow Ed.S.

```html
<!DOCTYPE html>
<html lang="en">
<head>
<meta charset="utf-8">
<title>LoomTrellis Stationery</title>
<link href="https://fonts.googleapis.com/css2?family=Montserrat:wght@400;600;800&display=swap" rel="stylesheet">
<style>
  :root{
    --ink:#1a1a1a;
    --black:#111111;
    --red:#c8102e;
    --yellow:#f5b400;
    --paper:#ffffff;
    --stage:#e6e3df;
    --muted:#d9d9d9;
  }
  *{box-sizing:border-box;margin:0;padding:0}
  html,body{width:1200px;height:852px;overflow:hidden}
  body{background:var(--stage);font-family:"Montserrat",sans-serif;position:relative;color:var(--ink)}
  .sheet{position:absolute;background:var(--paper);box-shadow:0 2px 8px rgba(0,0,0,.25);overflow:hidden}
  .swoosh{position:absolute;left:0;bottom:0;width:100%;display:block}
  .brand{display:flex;align-items:center;gap:8px;position:absolute}
  .brand-dot{border-radius:50%;background:var(--red);flex:none}
  .brand-name{font-weight:800;color:var(--ink);letter-spacing:.5px;white-space:nowrap}

  /* letterhead */
  .letterhead{left:80px;top:84px;width:486px;height:744px}
  .letterhead .brand{left:26px;top:26px}
  .letterhead .brand-dot{width:26px;height:26px}
  .letterhead .brand-name{font-size:24px}
  .letterhead-footer{position:absolute;right:22px;bottom:10px;text-align:right;color:#fff;font-size:8px;line-height:1.5}
  .letterhead-footer .row{display:flex;gap:12px;justify-content:flex-end}
  .icon{display:inline-block;width:6px;height:6px;border-radius:50%;background:var(--red);margin-right:3px;vertical-align:middle}

  /* business cards */
  .card{top:96px;width:192px;height:132px;background:var(--black);border-radius:6px}
  .card-front{left:667px}
  .card-back{left:883px}
  .card-front .mark{position:absolute;left:20px;top:24px;width:26px;height:26px;border-radius:50%;background:var(--red)}
  .card-back .brand{left:12px;top:34px;gap:6px}
  .card-back .brand-dot{width:18px;height:18px}
  .card-back .brand-name{font-size:15px;color:#fff}
  .card-person{position:absolute;right:10px;top:10px;text-align:right;font-size:6px;line-height:1.3}
  .card-person .name{color:var(--red);font-weight:600}
  .card-person .role{color:#cfcfcf}
  .card-contact{position:absolute;left:12px;top:70px;font-size:5.5px;color:#cfcfcf}

  /* envelopes */
  .envelope{left:600px;width:528px}
  .envelope-back{top:252px;height:288px}
  .envelope-front{top:564px;height:264px}
  .flap{position:absolute;left:0;top:0;width:100%;height:110px}
  .flap-mark{position:absolute;left:246px;top:22px;width:36px;height:36px;border-radius:50%;background:var(--red)}
  .envelope-front .brand{left:24px;top:22px}
  .envelope-front .brand-dot{width:24px;height:24px}
  .envelope-front .brand-name{font-size:22px}
  .return-address{position:absolute;left:56px;top:54px;font-size:7px;color:#444}
</style>
</head>
<body>

<section class="sheet letterhead">
  <div class="brand"><span class="brand-dot"></span><span class="brand-name">LoomTrellis</span></div>
  <svg class="swoosh" viewBox="0 0 500 150" preserveAspectRatio="none" height="150" aria-hidden="true">
    <path d="M0 64 C150 14 330 104 500 34 L500 150 L0 150Z" fill="var(--yellow)"/>
    <path d="M0 72 C150 22 330 112 500 42 L500 150 L0 150Z" fill="var(--paper)"/>
    <path d="M0 76 C150 26 330 116 500 46 L500 150 L0 150Z" fill="var(--red)"/>
    <path d="M0 86 C150 36 330 126 500 56 L500 150 L0 150Z" fill="var(--black)"/>
  </svg>
  <div class="letterhead-footer">
    <div>1402 Harbor Lane, Suite 5, Ashford, TN 38012</div>
    <div class="row">
      <span><span class="icon"></span>(555) 014-2271</span>
      <span><span class="icon"></span>hwinslow738@loomtrellis.com</span>
      <span><span class="icon"></span>www.loomtrellis.com</span>
    </div>
  </div>
</section>

<section class="sheet card card-front">
  <span class="mark"></span>
  <svg class="swoosh" viewBox="0 0 200 60" preserveAspectRatio="none" height="60" aria-hidden="true">
    <path d="M0 30 C60 8 130 48 200 18" stroke="var(--yellow)" stroke-width="2" fill="none"/>
    <path d="M0 36 C60 14 130 54 200 24" stroke="var(--red)" stroke-width="3" fill="none"/>
  </svg>
</section>

<section class="sheet card card-back">
  <div class="card-person"><div class="name">Howard Winslow Ed.S.</div><div class="role">Founding Director</div></div>
  <div class="brand"><span class="brand-dot"></span><span class="brand-name">LoomTrellis</span></div>
  <svg class="swoosh" viewBox="0 0 200 80" preserveAspectRatio="none" height="80" aria-hidden="true">
    <path d="M0 34 C60 12 130 52 200 22" stroke="var(--yellow)" stroke-width="2" fill="none"/>
    <path d="M0 40 C60 18 130 58 200 28" stroke="var(--red)" stroke-width="3" fill="none"/>
  </svg>
  <div class="card-contact">555 014 2271 · hwinslow738@loomtrellis.com · loomtrellis.com</div>
</section>

<section class="sheet envelope envelope-back">
  <svg class="flap" viewBox="0 0 528 110" preserveAspectRatio="none" aria-hidden="true">
    <path d="M0 0 L528 0 L528 8 L290 100 Q264 110 238 100 L0 8Z" fill="var(--black)"/>
  </svg>
  <span class="flap-mark"></span>
</section>

<section class="sheet envelope envelope-front">
  <div class="brand"><span class="brand-dot"></span><span class="brand-name">LoomTrellis</span></div>
  <div class="return-address">1402 Harbor Lane, Suite 5, Ashford, TN 38012</div>
  <svg class="swoosh" viewBox="0 0 528 90" preserveAspectRatio="none" height="90" aria-hidden="true">
    <path d="M0 30 C160 0 350 60 528 16 L528 90 L0 90Z" fill="var(--yellow)"/>
    <path d="M0 37 C160 7 350 67 528 23 L528 90 L0 90Z" fill="var(--paper)"/>
    <path d="M0 41 C160 11 350 71 528 27 L528 90 L0 90Z" fill="var(--red)"/>
    <path d="M0 50 C160 20 350 80 528 36 L528 90 L0 90Z" fill="var(--black)"/>
  </svg>
</section>

</body>
</html>
```